依頼詳細
分譲マンションのバルコニーの清掃のサービスをします。Before / After等の写真を載せ、プロにお願いするとこんなにも綺麗になるんだと自分で清掃するよりも魅力を感じてもらう為にもサービスを受けたいと思っていただけるようなチラシを作成していただきたいです。
記載項目
社名:株式会社ヨルダ
電話番号:06-6381-7942
住所:大阪市中央区朝霧町2-8-3
QRコード:作成次第送付します。
使用写真:添付
見出し:39(サンキュー)キャンペーン(オシャレな感じで文字ってください)
載せてほしい文言
・当社独自のバルコニークリーニング
・今、このチラシを受け取った
・このチラシを見ているあなた!今なら良いマンション作りに向けたアンケートにご協力していただいた方には、通常13,000円(税込)⇒なんと、3,900円(税込)!!
・作業時間:1H
・何かキャラクター等使用して吹き出しで、気になる箇所全て私達にお申し出ください!!
と記載してください。
自分の中のイメージ図を添付しますが、全然変更してもらっても大丈夫です。オシャレな感じに作成をお願いします。
サイズ
A4
ページ数
片面
希望イメージ
シンプル 複雑
単色 カラフル
暗い 明るい
日常 高級
遊び心 厳粛
未来的 伝統的
女性的 男性的
希望する色
水色系
納品ファイル
• イラストレーター形式 (.ai)
補足説明

私が求めているようなデザインを考案していただきました。

この度はありがとうございました。
どれも魅力的なものばかりで選定するのも困るくらいでした。
今後もお世話になるかと思いますので何卒宜しくお願い致します。

```html
<!DOCTYPE html>
<html lang="ja">
<head>
<meta charset="utf-8">
<title>39キャンペーン｜バルコニークリーニング</title>
<link rel="stylesheet" href="https://fonts.googleapis.com/css2?family=M+PLUS+Rounded+1c:wght@500;700;800;900&display=swap">
<style>
:root{
  --sky:#d3ecf9;
  --sky-stripe:#c6e5f7;
  --blue:#2b93d6;
  --blue-dark:#1678bf;
  --navy:#145f9e;
  --yellow:#ffe14a;
  --orange:#f2961b;
  --white:#ffffff;
  --ink:#2a5d8a;
  --grey:#9aa3ab;
}
*{margin:0;padding:0;box-sizing:border-box}
html,body{width:846px;height:1200px;overflow:hidden;background:var(--white)}
body{font-family:"M PLUS Rounded 1c",sans-serif;color:var(--ink)}
.flyer{position:relative;width:846px;height:1200px;overflow:hidden;
  background:repeating-linear-gradient(90deg,var(--sky) 0 22px,var(--sky-stripe) 22px 44px)}
.abs{position:absolute;white-space:nowrap}

.ribbon{left:120px;top:28px;width:606px;height:58px;background:var(--blue);color:var(--white);
  font-weight:800;font-size:28px;letter-spacing:2px;display:flex;align-items:center;justify-content:center;
  clip-path:polygon(0 0,100% 0,96% 50%,100% 100%,0 100%,4% 50%)}
.balcony-photo{left:90px;top:112px;width:205px;height:128px;border:5px solid var(--white);
  background:linear-gradient(160deg,#d9eef2,#8fbfa3 55%,#6f8f86)}

.title-ruby{left:0;width:846px;top:112px;text-align:center;font-weight:800;font-size:28px;color:var(--blue-dark);letter-spacing:4px}
.title-num{left:0;width:846px;top:140px;text-align:center;font-weight:900;font-size:160px;line-height:1;color:var(--yellow);
  -webkit-text-stroke:6px var(--blue-dark);paint-order:stroke fill;letter-spacing:-6px}
.title-main{left:0;width:846px;top:300px;text-align:center;font-weight:900;font-size:96px;line-height:1;color:var(--blue);
  -webkit-text-stroke:8px var(--white);paint-order:stroke fill;letter-spacing:2px}
.status{left:0;width:846px;top:410px;text-align:center;font-weight:900;font-size:38px;color:var(--navy)}

.building{left:612px;top:426px;width:186px;height:144px;background:linear-gradient(180deg,#c9b79a,#9c8669)}
.staff{left:300px;top:466px;width:250px;height:100px;background:linear-gradient(180deg,#9fd3f2,#4ea7df);border-radius:30px}

.promise{left:40px;top:574px;width:766px;height:56px;background:var(--blue);border-radius:8px;padding:6px}
.promise p{height:100%;background:var(--white);border-radius:6px;color:var(--blue-dark);font-weight:800;font-size:27px;
  display:flex;align-items:center;justify-content:center}

.offer-band{left:0;top:652px;width:846px;height:46px;background:var(--blue);color:var(--white);font-weight:700;font-size:20px;
  padding-left:40px;display:flex;align-items:center}
.limited{left:680px;top:640px;width:120px;height:58px;background:var(--white);border-radius:10px 10px 0 0;color:var(--blue-dark);
  font-weight:900;font-size:30px;display:flex;align-items:center;justify-content:center}
.offer{left:0;top:698px;width:846px;height:294px;background:var(--white)}

.ba{top:740px;width:152px;height:170px;border-radius:4px}
.ba.before{left:30px;background:linear-gradient(180deg,#8d8a84,#5e5a55)}
.ba.after{left:182px;background:linear-gradient(180deg,#b9c2c7,#8e989e)}
.ba-tag{bottom:8px;padding:2px 12px;font-size:16px;font-weight:700;color:var(--white);border-radius:3px;position:absolute}
.before .ba-tag{left:8px;background:#555}
.after .ba-tag{right:8px;background:var(--blue)}
.work-time{left:30px;top:916px;font-size:14px;font-weight:700;color:#555}

.regular{left:360px;top:714px;font-size:24px;font-weight:700;color:var(--ink)}
.now{left:360px;top:762px;display:flex;align-items:baseline;gap:10px;color:var(--ink)}
.now .lead{font-size:32px;font-weight:800}
.now .price{font-size:84px;font-weight:900;color:var(--orange);line-height:1;letter-spacing:-2px}
.now .unit{font-size:32px;font-weight:800;color:var(--orange)}
.now .tax{font-size:22px;font-weight:800}
.pun{left:520px;top:858px;font-size:22px;font-weight:800;color:var(--orange);letter-spacing:12px}

.bubble{left:454px;top:898px;width:168px;height:84px;background:var(--white);border:2px solid var(--blue);border-radius:42px;
  font-size:13px;font-weight:700;color:var(--blue-dark);text-align:center;display:flex;align-items:center;justify-content:center;line-height:1.4}
.helper{left:636px;top:896px;width:180px;height:92px;background:linear-gradient(180deg,#9fd3f2,#4ea7df);border-radius:24px}

.footer{left:0;top:992px;width:846px;height:208px;background:var(--blue)}
.company{left:36px;top:1034px;font-size:38px;font-weight:800;color:var(--white)}
.address{left:36px;top:1096px;font-size:18px;font-weight:700;color:var(--white)}
.phone{left:330px;top:1030px;display:flex;align-items:center;gap:12px;font-size:44px;font-weight:800;color:var(--white)}
.hours{left:396px;top:1098px;font-size:20px;font-weight:700;color:var(--white)}
.qr{left:700px;top:1030px;width:112px;height:112px;background:var(--grey)}
</style>
</head>
<body>
<main class="flyer">
  <div class="abs ribbon">当社独自のバルコニークリーニング</div>
  <div class="abs balcony-photo" role="img" aria-label="清掃後のバルコニーの写真"></div>

  <div class="abs title-ruby">サンキュー</div>
  <div class="abs title-num">39</div>
  <h1 class="abs title-main">キャンペーン</h1>
  <div class="abs status">実施中!!</div>

  <div class="abs building" role="img" aria-label="分譲マンションのイラスト"></div>
  <div class="abs staff" role="img" aria-label="清掃スタッフ3人のイラスト"></div>

  <div class="abs promise"><p>マンションのバルコニー清掃はプロにお任せください!</p></div>

  <div class="abs offer-band">より良いマンション作りに向けたアンケートにご協力いただいた方</div>
  <div class="abs limited">限定</div>
  <section class="abs offer"></section>

  <div class="abs ba before" role="img" aria-label="清掃前のバルコニー床の写真"><span class="ba-tag">Before</span></div>
  <div class="abs ba after" role="img" aria-label="清掃後のバルコニー床の写真"><span class="ba-tag">After</span></div>
  <div class="abs work-time">▲ 作業時間：約1時間</div>

  <p class="abs regular">通常 13,000円(税込)のところ</p>
  <p class="abs now"><span class="lead">今なら</span><span class="price">3,900</span><span class="unit">円</span><span class="tax">(税込)</span></p>
  <p class="abs pun">サンキュー</p>

  <div class="abs bubble">気になる箇所があれば<br>全て私たちに<br>お申し出ください</div>
  <div class="abs helper" role="img" aria-label="吹き出しで話す清掃スタッフのイラスト"></div>

  <footer class="abs footer"></footer>
  <p class="abs company">株式会社ヨルダ</p>
  <p class="abs address">大阪市中央区朝霧町2-8-3</p>
  <p class="abs phone">
    <svg width="42" height="42" viewBox="0 0 24 24" aria-hidden="true"><circle cx="12" cy="12" r="11" fill="none" stroke="#fff" stroke-width="2"/><path d="M8.2 6.5l1.8-.4 1.3 2.8-1.2 1a7 7 0 003.9 3.9l1-1.2 2.8 1.3-.4 1.8c-.2.7-.9 1.1-1.6 1A10 10 0 017.2 8.1c-.1-.7.3-1.4 1-1.6z" fill="#fff"/></svg>
    06-6381-7942
  </p>
  <p class="abs hours">営業時間：平日　0:00 ～ 0:00</p>
  <div class="abs qr" role="img" aria-label="QRコード掲載スペース"></div>
</main>
</body>
</html>
```